I am a home builder and developer

I would like some sort of architectural design like a pencil type of drawing of a house but want it to be professional looking and two sided.

Simply I am a custom home builder and land developer. I would like a new design other than what I have now that's what I thought y'all did. I like mostly black maybe with an pencil type of drawing of a house. Like an architectural look.

Industry/Entity Type

Home Builder

```html
<!DOCTYPE html>
<html lang="en">
<head>
<meta charset="utf-8">
<title>K&amp;R Building Inc — Business Card</title>
<link rel="stylesheet" href="https://fonts.googleapis.com/css2?family=Montserrat:wght@600&family=Open+Sans:wght@400;700&display=swap">
<style>
  :root {
    --brand-blue: #1f3f9a;
    --brand-grey: #6b6b6b;
    --sketch-light: #f0f0f0;
    --sketch-mid: #d9d9d9;
    --sketch-dark: #c4c4c4;
    --card-white: #ffffff;
    --ink: #2b2b2b;
    --backdrop: #e9e9ea;
  }
  * { box-sizing: border-box; margin: 0; padding: 0; }
  html, body { width: 1200px; height: 900px; overflow: hidden; }
  body {
    background: var(--backdrop);
    font-family: "Open Sans", Arial, sans-serif;
    position: relative;
  }
  .card {
    position: absolute;
    left: 250px;
    width: 700px;
    height: 400px;
    background: var(--card-white);
    overflow: hidden;
    box-shadow: 0 2px 6px rgba(0,0,0,0.12);
  }
  .card--front { top: 30px; }
  .card--back { top: 470px; }

  .house-sketch {
    position: absolute;
    left: 20px; right: 20px; top: 30px; bottom: 20px;
    background:
      radial-gradient(ellipse 38% 55% at 60% 55%, var(--sketch-dark) 0%, rgba(217,217,217,0.6) 55%, rgba(255,255,255,0) 100%),
      radial-gradient(ellipse 20% 35% at 12% 62%, var(--sketch-mid) 0%, rgba(255,255,255,0) 100%),
      radial-gradient(ellipse 18% 30% at 90% 68%, var(--sketch-mid) 0%, rgba(255,255,255,0) 100%),
      linear-gradient(180deg, var(--card-white) 0%, var(--sketch-light) 45%, var(--sketch-light) 85%, var(--card-white) 100%);
  }
  .wordmark {
    position: absolute;
    color: var(--brand-blue);
    font-family: "Montserrat", Arial, sans-serif;
    font-weight: 600;
    text-align: center;
    line-height: 1;
  }
  .wordmark__initials { display: block; font-size: 110px; letter-spacing: 2px; }
  .wordmark__name { display: block; font-size: 40px; letter-spacing: 1px; margin-top: 4px; }
  .card--front .wordmark { left: 0; right: 0; top: 115px; }
  .card--back .wordmark { right: 55px; top: 110px; }

  .corner-mark { position: absolute; left: 0; top: 0; }
  .holder-name {
    position: absolute;
    left: 62px; top: 34px;
    color: var(--brand-blue);
    font-weight: 700;
    font-size: 19px;
  }
  .contact-list {
    position: absolute;
    left: 48px; top: 178px;
    list-style: none;
    color: var(--ink);
    font-size: 17px;
  }
  .contact-list li { display: flex; align-items: center; gap: 10px; margin-bottom: 4px; }
  .contact-list svg { width: 13px; height: 13px; fill: var(--brand-blue); flex: none; }
  .bottom-bands { position: absolute; left: 0; top: 0; }
</style>
</head>
<body>
  <section class="card card--front">
    <div class="house-sketch" role="img" aria-label="Light grey pencil-style architectural drawing of a large Victorian house flanked by trees"></div>
    <div class="wordmark">
      <span class="wordmark__initials">K&amp;R</span>
      <span class="wordmark__name">BUILDING INC</span>
    </div>
  </section>

  <section class="card card--back">
    <svg class="bottom-bands" width="700" height="400" viewBox="0 0 700 400" aria-hidden="true">
      <polygon points="0,0 28,0 12,22 0,22" fill="var(--brand-blue)"/>
      <polygon points="36,0 52,0 52,22 20,22" fill="var(--brand-grey)"/>
      <polygon points="0,258 0,282 285,345 298,330" fill="var(--brand-blue)"/>
      <polygon points="318,338 700,338 700,400 300,400 300,356" fill="var(--brand-grey)"/>
    </svg>
    <p class="holder-name">Daniel Crane</p>

    <ul class="contact-list">
      <li>
        <svg viewBox="0 0 24 24" aria-hidden="true"><path d="M6.6 10.8a15.1 15.1 0 0 0 6.6 6.6l2.2-2.2a1 1 0 0 1 1-.25 11.4 11.4 0 0 0 3.6.57 1 1 0 0 1 1 1V20a1 1 0 0 1-1 1A17 17 0 0 1 3 4a1 1 0 0 1 1-1h3.5a1 1 0 0 1 1 1c0 1.25.2 2.45.57 3.6a1 1 0 0 1-.25 1z"/></svg>
        <span>555-014-2290</span>
      </li>
      <li>
        <svg viewBox="0 0 24 24" aria-hidden="true"><rect x="2" y="5" width="20" height="14"/><path d="M3 6l9 7 9-7" fill="none" stroke="#fff" stroke-width="1.6"/></svg>
        <span>krbuildinc@example.com</span>
      </li>
    </ul>

    <div class="wordmark">
      <span class="wordmark__initials">K&amp;R</span>
      <span class="wordmark__name">BUILDING INC</span>
    </div>
  </section>
</body>
</html>
```